Established food business needs a new name card design

Refer to attached current name card. Would like a new professional look design with only the company name and logo without any pictures. Would like green and yellow to be included.
To include:
My name "IBRAHIM SUKRI" and hand phone number "87260413".
To delete "
"Along Brackendale Ave 8" and
"www.nur-tiwas.com.sg"
To change email to:
"tkr27@velmorix.com.sg"

```html
<!DOCTYPE html>
<html lang="en">
<head>
<meta charset="UTF-8">
<title>Nur-Tiwas Eating Corner – Name Card</title>
<link href="https://fonts.googleapis.com/css2?family=Montserrat:wght@400;500;700;800&display=swap" rel="stylesheet">
<style>
  :root {
    --green: #104434;
    --yellow: #f2cf1d;
    --white: #ffffff;
    --stage: #dcdee0;
    --ink-light: #f4f4f0;
  }
  * { margin: 0; padding: 0; box-sizing: border-box; }
  html, body { width: 1200px; height: 800px; overflow: hidden; }
  body {
    background: linear-gradient(160deg, #eceeef 0%, var(--stage) 55%, #cfd2d4 100%);
    font-family: "Montserrat", sans-serif;
    position: relative;
  }
  .card {
    position: absolute;
    width: 600px;
    height: 340px;
    background: var(--green);
    overflow: hidden;
    box-shadow: 0 6px 18px rgba(0,0,0,0.18);
  }
  .card--front { left: 460px; top: 50px; }
  .card--back { left: 140px; top: 420px; }

  .brand { display: flex; align-items: center; gap: 14px; color: var(--yellow); }
  .brand__mark {
    width: 44px; height: 44px; border-radius: 50%;
    background: var(--yellow); flex: none;
  }
  .brand__name {
    font-weight: 800; font-size: 46px; letter-spacing: 1px; line-height: 1;
  }
  .brand__tagline {
    display: block; border-top: 2px solid var(--yellow);
    margin-top: 6px; padding-top: 3px;
    font-weight: 500; font-size: 13px; letter-spacing: 7px;
    text-align: center; color: var(--yellow);
  }
  .card--front .brand-lockup {
    position: absolute; left: 50%; top: 50%;
    transform: translate(-50%, -50%);
  }
  .card--back .brand-lockup {
    position: absolute; left: 36px; top: 40px;
  }
  .card--back .brand__name { font-size: 32px; }
  .card--back .brand__tagline { font-size: 10px; letter-spacing: 5px; }

  .back-disc {
    position: absolute; left: 270px; top: 60px;
    width: 420px; height: 420px;
  }
  .holder-name {
    position: absolute; left: 360px; top: 118px;
    font-weight: 800; font-size: 18px; letter-spacing: 0.5px;
    color: var(--green);
  }
  .contact {
    position: absolute; left: 36px; top: 160px;
    color: var(--ink-light); font-size: 15px; line-height: 1.4;
    list-style: none;
  }
  .contact__address { margin-bottom: 4px; }
  .contact__item { display: flex; align-items: center; gap: 8px; }
  .contact__icon { width: 14px; height: 14px; flex: none; }
</style>
</head>
<body>

<section class="card card--front" aria-label="Name card front">
  <div class="brand-lockup">
    <div class="brand">
      <span class="brand__mark" aria-hidden="true"></span>
      <span class="brand__name">NUR-TIWAS</span>
    </div>
    <span class="brand__tagline">EATING CORNER</span>
  </div>
</section>

<section class="card card--back" aria-label="Name card back">
  <svg class="back-disc" viewBox="0 0 420 420" aria-hidden="true">
    <circle cx="210" cy="210" r="196" fill="var(--white)" stroke="var(--yellow)" stroke-width="14"/>
  </svg>

  <div class="brand-lockup">
    <div class="brand">
      <span class="brand__name">NUR-TIWAS</span>
    </div>
    <span class="brand__tagline">EATING CORNER</span>
  </div>

  <p class="holder-name">IBRAHIM SUKRI</p>

  <ul class="contact">
    <li class="contact__address">48 Kelvora Industrial<br>Estate Road 2 # 02-14<br>Singapore 736184</li>
    <li class="contact__item">
      <svg class="contact__icon" viewBox="0 0 24 24" aria-hidden="true">
        <path fill="var(--yellow)" d="M6.6 10.8a15 15 0 0 0 6.6 6.6l2.2-2.2a1 1 0 0 1 1-.25 11.4 11.4 0 0 0 3.6.57 1 1 0 0 1 1 1V20a1 1 0 0 1-1 1A17 17 0 0 1 3 4a1 1 0 0 1 1-1h3.5a1 1 0 0 1 1 1c0 1.25.2 2.45.57 3.57a1 1 0 0 1-.25 1z"/>
      </svg>
      87260413
    </li>
    <li class="contact__item">
      <svg class="contact__icon" viewBox="0 0 24 24" aria-hidden="true">
        <rect x="2" y="5" width="20" height="14" fill="none" stroke="var(--yellow)" stroke-width="2.4"/>
        <path d="M2 5l10 8 10-8" fill="none" stroke="var(--yellow)" stroke-width="2.4"/>
      </svg>
      tkr27@velmorix.com.sg
    </li>
  </ul>
</section>

</body>
</html>
```